Barricade cover design needed for amusement ride exhibit

FunWagonz is a company that sells coin operated amusement rides for kids that look and function like construction equipment such as excavator diggers and cranes. We need a design for vinyl covers that go over steel barricade fences formed around our amusement ride booth. The amusement ride booth is called "Tiny Hauler Yard" and is meant to look like a construction site where the machines are used. The design should incorporate things related to the construction industry but also be geared towards kids, toys, and fun!

Target Market(s)

Kids and Families

Industry/Entity Type

Amusement Park

Colors
fbed22
ffc214
fece3e
faa54b
f78f20

Requirements
Must have
• "Tiny Hauler Yard", "Powered By FunWagonz"
Nice to have
• Male and Female Construction Characters, Caution Tape, Construction Signs

```html
<!DOCTYPE html>
<html lang="en">
<head>
<meta charset="utf-8">
<title>Tiny Hauler Yard – Barricade Cover</title>
<link rel="stylesheet" href="https://fonts.googleapis.com/css2?family=Alfa+Slab+One&display=swap">
<style>
  :root {
    --frame-steel: #2b2b2d;
    --frame-edge: #1a1a1b;
    --panel-black: #070707;
    --caution-yellow: #f2e31a;
    --caution-deep: #c9b512;
    --title-orange: #f05a28;
    --plate-light: #e4e5e7;
    --plate-mid: #b9bbbe;
    --plate-dark: #8e9094;
    --badge-olive: #b8ac3a;
    --ink: #111111;
  }
  html, body {
    margin: 0;
    padding: 0;
    width: 1200px;
    height: 566px;
    overflow: hidden;
    background: #e6e7e9;
  }
  .barricade-cover {
    position: relative;
    width: 1200px;
    height: 566px;
    background: var(--frame-steel);
    box-shadow: inset 0 0 0 3px var(--frame-edge);
  }
  .caution-panel {
    position: absolute;
    left: 41px;
    top: 41px;
    width: 1118px;
    height: 484px;
    border-radius: 14px;
    overflow: hidden;
    background: var(--panel-black);
  }
  .caution-panel svg { display: block; }
  .title {
    position: absolute;
    left: 230px;
    top: 176px;
    width: 640px;
    margin: 0;
    text-align: center;
    font-family: "Alfa Slab One", "Rockwell", serif;
    font-weight: 400;
    color: var(--title-orange);
    font-size: 86px;
    line-height: 94px;
    letter-spacing: 1px;
  }
  .title span { display: block; }
  .character {
    position: absolute;
    border-radius: 40px 40px 10px 10px;
  }
  .character--planner { left: 69px; top: 174px; width: 156px; height: 328px;
    background: linear-gradient(180deg, #f2cf2a 0%, #2f4f8a 45%, #1d1d22 100%); }
  .character--mechanic { left: 249px; top: 288px; width: 102px; height: 227px;
    background: linear-gradient(180deg, #f2cf2a 0%, #5a6c80 55%, #e9b21d 100%); }
  .character--worker { left: 772px; top: 283px; width: 87px; height: 228px;
    background: linear-gradient(180deg, #f2cf2a 0%, #f3a33a 40%, #2f6f9a 100%); }
  .character--architect { left: 868px; top: 286px; width: 97px; height: 235px;
    background: linear-gradient(180deg, #f2cf2a 0%, #c8232c 50%, #b01e26 100%); }
  .sponsor-badge {
    position: absolute;
    left: 912px;
    top: 229px;
    width: 247px;
    height: 113px;
    background: var(--badge-olive);
    clip-path: polygon(0 0, 100% 0, 100% 100%, 12% 100%);
    font-family: "Alfa Slab One", "Rockwell", serif;
    color: var(--ink);
  }
  .sponsor-badge .powered-by {
    position: absolute;
    left: 60px;
    top: 10px;
    font-size: 14px;
  }
  .sponsor-badge .sponsor-name {
    position: absolute;
    left: 28px;
    top: 34px;
    font-size: 34px;
    line-height: 40px;
  }
  .steel-plate {
    position: absolute;
    left: 0;
    width: 1200px;
    height: 107px;
    pointer-events: none;
  }
  .steel-plate--top { top: 0; }
  .steel-plate--bottom { top: 459px; }
</style>
</head>
<body>
<main class="barricade-cover">
  <section class="caution-panel">
    <svg width="1118" height="484" viewBox="0 0 1118 484" aria-hidden="true">
      <defs>
        <pattern id="caution-stripes" width="150" height="150" patternUnits="userSpaceOnUse" patternTransform="rotate(-40)">
          <rect width="150" height="150" fill="var(--panel-black)"/>
          <rect width="72" height="150" fill="var(--caution-yellow)"/>
        </pattern>
        <linearGradient id="stripe-fade" x1="0" x2="1">
          <stop offset="0" stop-color="#000" stop-opacity="0.55"/>
          <stop offset="0.5" stop-color="#000" stop-opacity="0"/>
          <stop offset="1" stop-color="#000" stop-opacity="0.55"/>
        </linearGradient>
      </defs>
      <rect class="stripe-band" x="0" y="0" width="1118" height="97" fill="url(#caution-stripes)"/>
      <rect class="stripe-band" x="0" y="304" width="1118" height="180" fill="url(#caution-stripes)"/>
      <rect x="0" y="0" width="1118" height="484" fill="url(#stripe-fade)"/>
      <rect class="title-band" x="0" y="97" width="1118" height="207" fill="var(--panel-black)"/>
    </svg>
  </section>

  <h1 class="title"><span>Tiny Hauler</span><span>Yard</span></h1>

  <div class="character character--planner" role="img" aria-label="Cartoon boy in a hard hat and suit reading blueprints"></div>
  <div class="character character--mechanic" role="img" aria-label="Cartoon kid in overalls and hard hat holding a screwdriver"></div>
  <div class="character character--worker" role="img" aria-label="Cartoon construction worker in safety vest and goggles giving a thumbs up"></div>
  <div class="character character--architect" role="img" aria-label="Cartoon girl in a hard hat and red suit carrying rolled plans"></div>

  <div class="sponsor-badge">
    <span class="powered-by">Powered By:</span>
    <span class="sponsor-name">FunWagonz</span>
  </div>

  <svg class="steel-plate steel-plate--top" viewBox="0 0 1200 107" aria-hidden="true">
    <defs>
      <linearGradient id="plate-sheen" x1="0" y1="0" x2="0" y2="1">
        <stop offset="0" stop-color="var(--plate-light)"/>
        <stop offset="0.7" stop-color="var(--plate-mid)"/>
        <stop offset="1" stop-color="var(--plate-dark)"/>
      </linearGradient>
    </defs>
    <path d="M405 0 H795 L783 94 Q781 106 768 106 H432 Q419 106 417 94 Z" fill="url(#plate-sheen)" stroke="#7d7f83" stroke-width="1.5"/>
    <polygon points="523,60 530,48 544,48 551,60 544,72 530,72" fill="#dfe1e4" stroke="#6f7176" stroke-width="2"/>
    <circle cx="537" cy="60" r="7" fill="#9c9ea2"/>
    <polygon points="808,60 815,48 829,48 836,60 829,72 815,72" fill="#dfe1e4" stroke="#6f7176" stroke-width="2" transform="translate(-150 0)"/>
    <circle cx="672" cy="60" r="7" fill="#9c9ea2"/>
  </svg>

  <svg class="steel-plate steel-plate--bottom" viewBox="0 0 1200 107" aria-hidden="true">
    <defs>
      <linearGradient id="plate-sheen-low" x1="0" y1="0" x2="0" y2="1">
        <stop offset="0" stop-color="var(--plate-light)"/>
        <stop offset="0.6" stop-color="var(--plate-mid)"/>
        <stop offset="1" stop-color="var(--plate-dark)"/>
      </linearGradient>
    </defs>
    <path d="M432 0 H768 Q781 0 783 12 L795 107 H405 L417 12 Q419 0 432 0 Z" fill="url(#plate-sheen-low)" stroke="#7d7f83" stroke-width="1.5"/>
    <polygon points="523,33 530,21 544,21 551,33 544,45 530,45" fill="#dfe1e4" stroke="#6f7176" stroke-width="2"/>
    <circle cx="537" cy="33" r="7" fill="#9c9ea2"/>
    <polygon points="658,33 665,21 679,21 686,33 679,45 665,45" fill="#dfe1e4" stroke="#6f7176" stroke-width="2"/>
    <circle cx="672" cy="33" r="7" fill="#9c9ea2"/>
  </svg>
</main>
</body>
</html>
```